Hello,
We’re looking for a new WordPress website for Gather Your Light, our company offering unique well-being retreats and workshops.
We currently have a website online (you can consult it : www.gatheryourlight.ch), but we now need to build a new site on WordPress — more flexible, more intuitive to manage, and better aligned with our evolving needs.

What we’re looking for:
A new userfriendly WordPress site, with:
Inspiring, elegant, and modern design
Smooth user experience on desktop and mobile
Innovative design proposals – we want to be inspired !
SEO best practices
Respect of our existing color palette
The final website will need to be set up on our existing hosting provider (details can be shared later)

Pages to Include:
- Home
- Our Story
- Our Stays - with links to 5 individual pages, each describing one of our stays in detail.
- Activities – with potential links to individual descriptive pages
- Agenda
- Our Charter
- The Team
- Contact
- Blog

Required Features:
- Space for photos and videos
- Sections for testimonials and press articles
- Blog/article layout with strong readability
- Easy-to-update backend for future content
- Newsletter sign-up (pop-up and in footer)
- Additional pop-up on/off
- “Request info” buttons
- “Booking request” buttons
- Integration of our 4 pillars - Breathe · Feel · Connect · Experience - in the design (They’re currently in the footer, but we’re open to creative suggestions)

Who we are :
Gather Your Light offers well-being and personal growth stays but with a very different spirit.
We’re not a classic wellness brand. Our approach is professional, joyful, and grounded.
We create spaces where people can take a real break — breathe, slow down, and reconnect with themselves.
During our stays, people are welcomed like friends:
with warmth, respect, and no pressure.
Each program combines practices like breathwork, movement, creativity, coaching, and massages in a relaxed, beautiful setting of the French Alps.
What makes us different:
A friendly and down-to-earth atmosphere
A wide mix of activities.
A mix of inner work and simple pleasures
Private rooms, nourishing food, and shared moments
Time to talk, to laugh, to walk, or just be silent together - and feel free to be yourself
Our guests come to pause.
They leave feeling lighter, aligned, and full of life

```html
<!DOCTYPE html>
<html lang="en">
<head>
<meta charset="utf-8">
<title>Gather Your Light — Well-Being Retreats</title>
<link href="https://fonts.googleapis.com/css2?family=Archivo:wght@700;800;900&family=Inter:wght@400;500;600&display=swap" rel="stylesheet">
<style>
:root{
  --navy:#232d6b;
  --navy-deep:#1c2459;
  --teal:#62c9c3;
  --ink:#111a3a;
  --text:#4a4f63;
  --page:#fafafb;
  --canvas:#eaecef;
  --white:#ffffff;
  --star:#f0a21f;
  --head:"Archivo",Arial,sans-serif;
  --body:"Inter",Arial,sans-serif;
}
*{margin:0;padding:0;box-sizing:border-box}
html,body{width:1200px;height:4087px;overflow:hidden;background:var(--canvas);font-family:var(--body);color:var(--ink)}
.page{position:absolute;left:79px;top:78px;width:1042px;height:3933px;background:var(--page);overflow:hidden}
section,header,footer{position:absolute;left:0;width:1042px}
.abs{position:absolute}
.stripes{background-color:var(--navy);background-image:repeating-linear-gradient(135deg,rgba(255,255,255,.025) 0 2px,transparent 2px 9px)}
.btn{position:absolute;display:flex;align-items:center;justify-content:center;border-radius:20px;background:var(--teal);color:var(--white);font-family:var(--head);font-weight:800;font-size:10px;letter-spacing:.3px;text-transform:uppercase}
.btn.dark{background:var(--ink)}
h2.title{position:absolute;font-family:var(--head);font-weight:900;font-size:27px;text-transform:uppercase;letter-spacing:-.3px;color:var(--ink)}
.on-navy{color:var(--white)!important}
p.copy{position:absolute;font-size:11.5px;line-height:22px;color:var(--text)}

/* header */
.site-header{top:0;height:54px;background:var(--white)}
.brand{position:absolute;left:131px;top:16px;font-family:var(--head);font-weight:800;font-size:20px;color:var(--navy);letter-spacing:.5px}
.nav a{position:absolute;top:21px;font-size:9.5px;color:var(--ink);text-decoration:none}
.nav a.active{text-decoration:underline;font-weight:600}
.nav .chev{display:inline-block;width:5px;height:5px;border-right:1px solid var(--ink);border-bottom:1px solid var(--ink);transform:rotate(45deg);margin-left:6px;position:relative;top:-2px}
.divider{position:absolute;left:827px;top:18px;width:1px;height:18px;background:var(--ink)}
.lang{position:absolute;left:873px;top:21px;font-size:9.5px}
.globe{position:absolute;left:891px;top:16px;width:22px;height:22px;border-radius:50%;background:var(--teal)}

/* hero */
.hero{top:54px;height:541px}
.hero-photo{position:absolute;inset:0;background:linear-gradient(100deg,#07090f 0%,#1a2230 30%,#4f5d6e 52%,#8796a6 70%,#5f7a54 100%)}
.hero-shade{position:absolute;inset:0;background:linear-gradient(90deg,rgba(0,0,0,.55),rgba(0,0,0,0) 60%)}
.hero-pill{position:absolute;left:137px;top:101px;height:24px;padding:0 20px;border-radius:14px;background:rgba(255,255,255,.14);color:var(--white);font-size:10px;display:flex;align-items:center}
.hero h1{position:absolute;left:131px;top:136px;font-family:var(--head);font-weight:900;font-size:35px;line-height:46px;color:var(--white);letter-spacing:-.5px}
.hero-sub{position:absolute;left:131px;top:286px;font-size:11.5px;line-height:19px;color:var(--white);width:380px}
.link-btn{position:absolute;left:311px;top:349px;font-family:var(--head);font-weight:800;font-size:10px;color:var(--white);text-decoration:underline}
.hero-word{position:absolute;left:10px;top:462px;font-family:var(--head);font-weight:900;font-size:86px;line-height:86px;color:rgba(255,255,255,.1);white-space:nowrap}

/* pillars */
.pillars{top:595px;height:360px}
.pillar{position:absolute;width:182px;height:179px;display:flex;flex-direction:column;align-items:center;background-image:repeating-linear-gradient(135deg,rgba(255,255,255,.035) 0 2px,transparent 2px 9px)}
.pillar.navy{background-color:var(--navy);top:76px}
.pillar.teal{background-color:var(--teal);top:122px}
.pillar .ico{margin-top:36px;width:42px;height:42px;border-radius:50%;background:var(--white);display:flex;align-items:center;justify-content:center}
.pillar .dash{margin-top:16px;width:64px;border-top:1.5px dashed var(--white)}
.pillar .name{margin-top:18px;font-family:var(--head);font-weight:900;font-size:15px;color:var(--white)}
.pillar.teal .dash{border-color:var(--ink)}
.pillar.teal .name{color:var(--ink)}

/* about */
.about{top:955px;height:486px}
.outline-title{position:absolute;left:135px;top:20px;font-family:var(--head);font-weight:800;font-size:68px;letter-spacing:-1px;color:transparent;-webkit-text-stroke:1.2px #8d91a6}
.sub-head{position:absolute;font-family:var(--head);font-weight:900;font-size:15px;color:var(--ink)}
.about-photo{position:absolute;left:580px;top:29px;width:331px;height:370px;background:linear-gradient(180deg,#c9d4e0 0%,#8a9bb0 30%,#5e7062 55%,#4d7a3a 80%,#3e6a30 100%)}

/* stays */
.stays{top:1441px;height:631px}
.stays-band{position:absolute;left:0;top:0;width:1042px;height:425px}
.vertical-word{position:absolute;left:-106px;top:180px;width:364px;transform:rotate(-90deg);font-family:var(--head);font-weight:800;font-size:58px;color:transparent;-webkit-text-stroke:1.2px rgba(255,255,255,.35);white-space:nowrap;text-align:center}
.stay-sub{color:rgba(255,255,255,.75)!important}
.stay-card{position:absolute;top:197px;width:250px;height:401px;background:var(--white);box-shadow:0 2px 10px rgba(17,26,58,.05)}
.stay-photo{height:228px}
.stay-card h3{position:absolute;left:29px;top:256px;font-family:var(--head);font-weight:900;font-size:15px}
.stay-card p{position:absolute;left:29px;top:284px;width:200px;font-size:10.5px;line-height:18px;color:var(--text)}
.stay-card .btn{left:29px;top:344px;width:144px;height:27px}

/* activities */
.activities{top:2072px;height:457px}
.activity{position:absolute;top:154px;width:182px;height:216px;background:var(--white);box-shadow:0 2px 10px rgba(17,26,58,.04)}
.activity .num{position:absolute;left:26px;top:37px;width:32px;height:32px;border-radius:50%;border:1px solid #c8cbd6;display:flex;align-items:center;justify-content:center;font-weight:600;font-size:11px}
.activity .num.on{background:var(--teal);border-color:var(--teal);color:var(--ink)}
.activity h3{position:absolute;left:26px;top:90px;font-family:var(--head);font-weight:900;font-size:15px}
.activity p{position:absolute;left:26px;top:128px;width:130px;font-size:10.5px;line-height:18px;color:var(--text)}

/* testimonials */
.guests{top:2529px;height:670px}
.guests-band{position:absolute;left:0;top:0;width:1042px;height:321px}
.guest-photo{position:absolute;top:169px;width:382px;height:303px}
.quote-card{position:absolute;top:373px;width:348px;height:151px;background:var(--white);box-shadow:0 3px 14px rgba(17,26,58,.06)}
.quote-card .rating{position:absolute;left:32px;top:22px;font-size:10px}
.quote-card .stars{position:absolute;left:31px;top:36px}
.quote-card .mark{position:absolute;right:32px;top:22px}
.quote-card blockquote{position:absolute;left:32px;top:72px;width:285px;font-size:10.5px;line-height:18px;font-style:italic;color:var(--ink)}
.dots{position:absolute;left:489px;top:569px;display:flex;gap:7px;align-items:center}
.dots i{display:block;width:5px;height:5px;border-radius:50%;background:#d4e9e8}
.dots i.on{width:11px;height:11px;background:var(--teal)}

/* stories */
.stories{top:3199px;height:295px;background:var(--white)}
.stories-photo{position:absolute;left:529px;top:0;width:513px;height:295px;background:linear-gradient(180deg,#b9c9d8 0%,#7a8d7c 30%,#4f8a3c 55%,#6aa24a 80%,#7cb35a 100%)}

/* footer */
.site-footer{top:3494px;height:439px}
.news-title{position:absolute;left:131px;top:44px;font-family:var(--head);font-weight:900;font-size:19px;line-height:28px;color:var(--white)}
.news-field{position:absolute;left:521px;top:46px;width:390px;height:34px;border-radius:20px;background:var(--navy-deep);border:1px solid rgba(255,255,255,.12)}
.news-field span{position:absolute;left:22px;top:11px;font-size:9.5px;color:var(--white)}
.news-field .btn{right:0;top:0;width:144px;height:32px;font-size:10px}
.rule{position:absolute;left:131px;width:786px;height:1px;background:rgba(255,255,255,.2)}
.foot-brand{position:absolute;left:131px;top:190px;font-family:var(--head);font-weight:800;font-size:26px;color:var(--white);letter-spacing:.5px}
.foot-about{position:absolute;left:131px;top:268px;width:240px;font-size:10px;line-height:18px;color:rgba(255,255,255,.8)}
.foot-col{position:absolute}
.foot-col h4{font-family:var(--head);font-weight:900;font-size:14px;color:var(--white);margin-bottom:12px}
.foot-col a,.foot-col span{display:block;font-size:10px;color:rgba(255,255,255,.8);text-decoration:none;line-height:27px}
.contact span{line-height:17.5px}
.foot-word{position:absolute;left:250px;top:355px;font-family:var(--head);font-weight:900;font-size:86px;line-height:86px;color:rgba(255,255,255,.05);white-space:nowrap}
.legal{position:absolute;top:414px;font-size:9px;color:rgba(255,255,255,.8)}
</style>
</head>
<body>
<div class="page">

  <header class="site-header">
    <div class="brand">GATHER</div>
    <nav class="nav">
      <a class="active" style="left:289px">Home</a>
      <a style="left:342px">Our Story</a>
      <a style="left:410px">Our Stays<span class="chev"></span></a>
      <a style="left:494px">Activities<span class="chev"></span></a>
      <a style="left:575px">Our Charter</a>
      <a style="left:653px">Agenda</a>
      <a style="left:713px">Team</a>
      <a style="left:764px">Blog</a>
    </nav>
    <div class="divider"></div>
    <div class="lang">En</div>
    <div class="globe"></div>
  </header>

  <section class="hero">
    <div class="hero-photo" role="img" aria-label="Hiker in a blue jacket sitting on a grassy ridge facing jagged alpine peaks"></div>
    <div class="hero-shade"></div>
    <div class="hero-pill">Welcome To Gather Your Light</div>
    <h1>TAKE A REAL BREAK<br>BREATHE, SLOW DOWN,<br>RECONNECT</h1>
    <p class="hero-sub">Unique Well-Being Retreats In The French Alps, Where You're Welcomed Like A Friend.</p>
    <div class="btn" style="left:131px;top:341px;width:157px;height:26px">Booking Request</div>
    <div class="link-btn">EXPLORE OUR STAYS</div>
    <div class="hero-word">GATHER YOUR LIGHT</div>
  </section>

  <section class="pillars">
    <div class="pillar navy" style="left:131px">
      <div class="ico"><svg width="22" height="22" viewBox="0 0 24 24" fill="none" stroke="#232d6b" stroke-width="2.2" stroke-linecap="round"><path d="M3 8h11a3 3 0 1 0-3-3"/><path d="M3 12h16a3 3 0 1 1-3 3"/><path d="M3 16h8"/></svg></div>
      <div class="dash"></div><div class="name">BREATHE</div>
    </div>
    <div class="pillar teal" style="left:330px">
      <div class="ico"><svg width="22" height="22" viewBox="0 0 24 24"><path d="M12 21s-8-5.2-8-11a4.5 4.5 0 0 1 8-2.8A4.5 4.5 0 0 1 20 10c0 5.8-8 11-8 11z" fill="#62c9c3"/></svg></div>
      <div class="dash"></div><div class="name">FEEL</div>
    </div>
    <div class="pillar navy" style="left:530px">
      <div class="ico"><svg width="22" height="22" viewBox="0 0 24 24" fill="#232d6b" stroke="#232d6b" stroke-width="1.8"><circle cx="17" cy="6" r="2.6"/><circle cx="7" cy="12" r="2.6"/><circle cx="17" cy="18" r="2.6"/><path d="M9.3 10.8l5.4-3.4M9.3 13.2l5.4 3.4" fill="none"/></svg></div>
      <div class="dash"></div><div class="name">CONNECT</div>
    </div>
    <div class="pillar teal" style="left:729px">
      <div class="ico"><svg width="24" height="24" viewBox="0 0 24 24" fill="none" stroke="#62c9c3" stroke-width="2"><circle cx="12" cy="12" r="10"/><path d="M12 6.5l1.7 3.6 3.9.5-2.9 2.7.8 3.9-3.5-2-3.5 2 .8-3.9-2.9-2.7 3.9-.5z" stroke-linejoin="round"/></svg></div>
      <div class="dash"></div><div class="name">EXPERIENCE</div>
    </div>
  </section>

  <section class="about">
    <div class="outline-title">ABOUT US</div>
    <h2 class="title" style="left:131px;top:130px">WHO WE ARE</h2>
    <p class="copy" style="left:131px;top:183px;width:380px">We're Not Your Classic Wellness Retreat — We're A Warm Community Inviting You To Pause, Feel, Connect, And Experience True Restoration</p>
    <div class="btn" style="left:131px;top:275px;width:125px;height:27px">Learn More</div>
    <div class="sub-head" style="left:131px;top:333px">MISSION</div>
    <p class="copy" style="left:131px;top:361px;width:200px;line-height:18px">Lorem Ipsum Dolor Sit Amet Proin Consequat Imperdiet.</p>
    <div class="sub-head" style="left:346px;top:333px">VISION</div>
    <p class="copy" style="left:346px;top:361px;width:200px;line-height:18px">Lorem Ipsum Dolor Sit Amet Proin Consequat Imperdiet.</p>
    <div class="about-photo" role="img" aria-label="Snow-capped mountain rising above green alpine meadows"></div>
  </section>

  <section class="stays">
    <div class="stays-band stripes"></div>
    <div class="vertical-word">OUR STAYS</div>
    <h2 class="title on-navy" style="left:131px;top:64px">FIND YOUR PERFECT STAY</h2>
    <p class="copy stay-sub" style="left:131px;top:110px;width:420px">Five Unique Stays Designed For Your Well-Being — Each One A Chance To Gather Your Light And Come Home To Yourself</p>
    <div class="btn" style="left:767px;top:97px;width:144px;height:26px">View All Stays</div>

    <article class="stay-card" style="left:131px">
      <div class="stay-photo" role="img" aria-label="Green alpine valley with a village below rocky peaks and blue sky" style="background:linear-gradient(180deg,#4f8fd6 0%,#8fb9e6 35%,#7a9a6a 60%,#4b8b2e 100%)"></div>
      <h3>PLACE 01</h3>
      <p>Lorem Ipsum Dolor Sit Amet Vitae Sit Habitant Enim. Sit Amet</p>
      <div class="btn">Discover More</div>
    </article>
    <article class="stay-card" style="left:397px">
      <div class="stay-photo" role="img" aria-label="Rocky mountain summit above a forested green pasture" style="background:linear-gradient(180deg,#f3f4f6 0%,#b9bec4 35%,#6f7a62 60%,#3f7d2b 100%)"></div>
      <h3>PLACE 02</h3>
      <p>Lorem Ipsum Dolor Sit Amet Vitae Sit Habitant Enim. Sit Amet</p>
      <div class="btn dark">Discover More</div>
    </article>
    <article class="stay-card" style="left:662px">
      <div class="stay-photo" role="img" aria-label="Snowy jagged peaks under a deep blue sky" style="background:linear-gradient(180deg,#2f5cb0 0%,#5b84c9 35%,#c3c8cf 60%,#6f7a6a 100%)"></div>
      <h3>PLACE 03</h3>
      <p>Lorem Ipsum Dolor Sit Amet Vitae Sit Habitant Enim. Sit Amet</p>
      <div class="btn">Discover More</div>
    </article>
    <article class="stay-card" style="left:927px">
      <div class="stay-photo" role="img" aria-label="Alpine slope with pine trees and distant snowy ridges" style="background:linear-gradient(180deg,#dbe5ef 0%,#9fb2c4 35%,#5e8a48 65%,#3d6b2a 100%)"></div>
      <h3>PLACE 04</h3>
      <p>Lorem Ipsum Dolor Sit Amet Vitae Sit Habitant Enim. Sit Amet</p>
      <div class="btn">Discover More</div>
    </article>
  </section>

  <section class="activities">
    <h2 class="title" style="left:131px;top:50px">A WIDE MIX OF ACTIVITIES</h2>
    <p class="copy" style="left:131px;top:90px;width:780px">From Breathwork And Movement To Creativity And Coaching — Our Programs Blend Inner Work With Simple Pleasures.</p>
    <div class="activity" style="left:131px"><div class="num">1</div><h3>BREATHWORK</h3><p>Lorem Ipsum Dolor Sit Amet Purus Urna Viverra Sodales Leo .</p></div>
    <div class="activity" style="left:330px"><div class="num on">2</div><h3>YOGA</h3><p>Lorem Ipsum Dolor Sit Amet Purus Urna Viverra Sodales Leo .</p></div>
    <div class="activity" style="left:530px"><div class="num">3</div><h3>WORKSHOPS</h3><p>Lorem Ipsum Dolor Sit Amet Purus Urna Viverra Sodales Leo .</p></div>
    <div class="activity" style="left:729px"><div class="num">4</div><h3>NATURE WALKS</h3><p>Lorem Ipsum Dolor Sit Amet Purus Urna Viverra Sodales Leo .</p></div>
  </section>

  <section class="guests">
    <div class="guests-band stripes"></div>
    <h2 class="title on-navy" style="left:131px;top:64px">WHAT OUR GUESTS SAY</h2>
    <p class="copy" style="left:131px;top:104px;width:600px;color:rgba(255,255,255,.8)">Lorem Ipsum Dolor Sit Amet Consectetur. Odio Enim Lectus Sagittis Iaculis.</p>
    <div class="btn" style="left:805px;top:82px;width:106px;height:27px">View All</div>

    <div class="guest-photo" style="left:131px;background:linear-gradient(180deg,#c7cf6a 0%,#a8b84a 45%,#7f9a3a 100%)" role="img" aria-label="Guest relaxing in a sunlit field of tall green grass"></div>
    <div class="guest-photo" style="left:529px;background:linear-gradient(180deg,#9fb4b8 0%,#6f8a76 35%,#3f8a9a 55%,#5b7a44 100%)" role="img" aria-label="Guest seated above a turquoise mountain lake"></div>

    <div class="quote-card" style="left:148px">
      <div class="rating">5.0 Rating</div>
      <svg class="stars" width="90" height="14" viewBox="0 0 90 14" fill="#f0a21f"><g id="s"><path d="M7 1l1.8 3.8 4.1.5-3 2.8.8 4.1L7 10.2 3.3 12.2l.8-4.1-3-2.8 4.1-.5z"/></g><use href="#s" x="18"/><use href="#s" x="36"/><use href="#s" x="54"/><use href="#s" x="72"/></svg>
      <svg class="mark" width="26" height="20" viewBox="0 0 26 20" fill="#62c9c3"><path d="M0 20V10C0 4 3 1 9 0v4c-3 1-4 3-4 6h5v10zM15 20V10c0-6 3-9 9-10v4c-3 1-4 3-4 6h5v10z"/></svg>
      <blockquote>Lorem Ipsum Dolor Sit Amet Consectetur. Nam Ac In Enim Vestibulum Eget. Lacus Eget Scelerisque Magna Facilisis Nisl Pretium. Pretium Vel.</blockquote>
    </div>
    <div class="quote-card" style="left:546px">
      <div class="rating">5.0 Rating</div>
      <svg class="stars" width="90" height="14" viewBox="0 0 90 14" fill="#f0a21f"><use href="#s"/><use href="#s" x="18"/><use href="#s" x="36"/><use href="#s" x="54"/><use href="#s" x="72"/></svg>
      <svg class="mark" width="26" height="20" viewBox="0 0 26 20" fill="#62c9c3"><path d="M0 20V10C0 4 3 1 9 0v4c-3 1-4 3-4 6h5v10zM15 20V10c0-6 3-9 9-10v4c-3 1-4 3-4 6h5v10z"/></svg>
      <blockquote>Lorem Ipsum Dolor Sit Amet Consectetur. Nam Ac In Enim Vestibulum Eget. Lacus Eget Scelerisque Magna Facilisis Nisl Pretium. Pretium Vel.</blockquote>
    </div>
    <div class="dots"><i></i><i></i><i class="on"></i><i></i><i></i></div>
  </section>

  <section class="stories">
    <h2 class="title" style="left:131px;top:72px">STORIES &amp; INSPIRATION</h2>
    <p class="copy" style="left:131px;top:112px;width:320px">Take A Moment To Pause — Read Our Thoughts, Stories, And Tips For Living Lighter, Feeling Deeper, And Staying Connected To Yourself</p>
    <div class="btn" style="left:131px;top:192px;width:131px;height:26px">Read Stories</div>
    <div class="stories-photo" role="img" aria-label="Alpine village with a chapel in a green valley beneath rocky peaks"></div>
  </section>

  <footer class="site-footer stripes">
    <div class="news-title">GATHER YOUR LIGHT — IN<br>YOUR INBOX</div>
    <div class="news-field"><span>Enter You Email</span><div class="btn">Join The Circle</div></div>
    <div class="rule" style="top:124px"></div>

    <div class="foot-word">H YOUR LIGHT</div>
    <div class="foot-brand">GATHER</div>
    <p class="foot-about">We're Not Your Classic Wellness Retreat — We're A Warm Community Inviting You To Pause, Feel, Connect, And Experience True Restoration</p>

    <div class="foot-col" style="left:446px;top:186px">
      <h4>LINKS</h4>
      <a>Home</a><a>Our Story</a><a>Our Stays</a><a>Activities</a>
    </div>
    <div class="foot-col" style="left:599px;top:180px">
      <a>Agenda</a><a>Our Charter</a><a>The Team</a><a>Blog</a><a>Contact</a>
    </div>
    <div class="foot-col contact" style="left:753px;top:186px">
      <h4>CONTACT US</h4>
      <span>Gather Your Light Sàrl Chemin</span>
      <span>Des Mélèzes 14 Bâtiment B2</span>
      <span>CH - 1884 Villars</span>
      <span style="margin-top:11px">Info@Gatheryourlight.Ch</span>
      <span style="margin-top:9px">+(415)-555-0142</span>
    </div>

    <div class="rule" style="top:400px"></div>
    <div class="legal" style="left:131px">Copyright © 2025 Gather Your Light . All Rights Reserved.</div>
    <div class="legal" style="left:791px">Privacy Policy &amp; Terms Of Condition</div>
  </footer>

</div>
</body>
</html>
```